Bref créative
see logo info from logo info
Bluefern Trading Partners, Ltd.
Use same font as used in my logo
can also give other font suggestions
Modern
Daniel Okafor
President
742 Hollis St. - Suite 0830
New York, NY 10093
212-555-0147 Ext-305
sales@bluefernexample.com
bluefernexample.com
we are looking for business card and stationary design layouts.
logo with name
This is our logo to be used for the layout of the business cards and stationary.

```html
<!DOCTYPE html>
<html lang="en">
<head>
<meta charset="utf-8">
<title>Bluefern Trading Partners — Stationery Concepts</title>
<link rel="stylesheet" href="https://fonts.googleapis.com/css2?family=Cinzel:wght@700&family=Open+Sans:wght@400;600&display=swap">
<style>
  :root {
    --brand-blue: #1f4fa8;
    --brand-navy: #1c2f63;
    --swoosh-dark: #1b1e2b;
    --paper: #ffffff;
    --paper-shade: #eef0f4;
    --backdrop: #ece7df;
    --ink: #3a3f4d;
    --label: #6b6457;
    --faint-mark: #e6eaf2;
  }
  * { box-sizing: border-box; margin: 0; padding: 0; }
  html, body { width: 1200px; height: 446px; overflow: hidden; }
  body {
    position: relative;
    background: var(--backdrop);
    font-family: "Open Sans", Arial, sans-serif;
    color: var(--ink);
  }
  .piece {
    position: absolute;
    background: var(--paper);
    box-shadow: 0 1px 4px rgba(0,0,0,.18);
    overflow: hidden;
  }
  .label {
    position: absolute;
    font-size: 6px;
    letter-spacing: .3px;
    text-transform: uppercase;
    color: var(--label);
  }
  .label--section { font-size: 7px; font-weight: 600; }

  .brand {
    display: flex;
    align-items: center;
    gap: 4px;
    font-family: "Cinzel", Georgia, serif;
    font-weight: 700;
    color: var(--brand-navy);
    line-height: 1.05;
  }
  .brand__dot {
    flex: none;
    border-radius: 50%;
    background: var(--brand-blue);
  }

  .wave { position: absolute; left: 0; bottom: 0; width: 100%; display: block; }

  /* Business cards */
  .card-front { left: 12px; top: 211px; width: 96px; height: 58px; }
  .card-front .brand { position: absolute; left: 10px; top: 8px; font-size: 5.2px; }
  .card-front .brand__dot { width: 8px; height: 8px; }
  .card-front .contact { position: absolute; left: 10px; top: 24px; font-size: 3.2px; line-height: 1.35; }
  .card-back { left: 12px; top: 288px; width: 96px; height: 54px; background: var(--brand-blue); display: flex; align-items: center; justify-content: center; }
  .card-back .brand { color: var(--paper); font-size: 5.6px; }
  .card-back .brand__dot { width: 10px; height: 10px; background: var(--paper); }

  /* Letterheads */
  .letterhead { top: 12px; width: 285px; height: 408px; }
  .letterhead--one { left: 148px; }
  .letterhead--two { left: 476px; }
  .letterhead .brand { position: absolute; left: 18px; top: 18px; font-size: 7px; }
  .letterhead .brand__dot { width: 12px; height: 12px; }
  .letterhead .contact { position: absolute; right: 22px; top: 16px; font-size: 4.2px; line-height: 1.5; text-align: left; }
  .letterhead--two .brand { left: 50%; transform: translateX(-50%); flex-direction: column; text-align: center; top: 16px; }
  .faint-mark {
    position: absolute; left: 50%; top: 48%;
    width: 120px; height: 120px; margin: -60px 0 0 -60px;
    border-radius: 50%; background: var(--faint-mark);
  }

  /* Envelopes */
  .envelope-back { left: 842px; width: 346px; height: 64px; background: var(--paper-shade); }
  .envelope-back--white { top: 12px; }
  .envelope-back--dark { top: 90px; }
  .envelope-back--blue { top: 168px; }
  .envelope-back .flap { position: absolute; left: 0; top: 0; width: 100%; height: 100%; }
  .envelope-back .brand { position: absolute; left: 50%; top: 34px; transform: translateX(-50%); font-size: 5px; }
  .envelope-back .brand__dot { width: 9px; height: 9px; }
  .envelope-back--dark .brand { color: var(--paper); }
  .envelope-back--dark .brand__dot { background: var(--paper); }

  .envelope-front { left: 792px; top: 252px; width: 356px; height: 156px; }
  .envelope-front .brand { position: absolute; left: 14px; top: 12px; font-size: 6px; }
  .envelope-front .brand__dot { width: 10px; height: 10px; }
  .envelope-front .contact { position: absolute; left: 14px; top: 30px; font-size: 3.6px; line-height: 1.4; }
</style>
</head>
<body>

  <span class="label label--section" style="left:12px; top:198px;">Stationery Concepts</span>

  <!-- Business card front -->
  <div class="piece card-front">
    <div class="brand"><span class="brand__dot"></span><span>Bluefern Trading<br>Partners, Ltd.</span></div>
    <div class="contact">
      <strong>Daniel Okafor</strong> · President<br>
      742 Hollis St. - Suite 0830<br>
      New York, NY 10093<br>
      212-555-0147 Ext-305<br>
      sales@bluefernexample.com
    </div>
    <svg class="wave" viewBox="0 0 96 14" preserveAspectRatio="none" aria-hidden="true">
      <path d="M0 6 C30 14 60 2 96 4 L96 14 L0 14Z" fill="var(--brand-blue)"/>
      <path d="M0 4 C30 12 60 0 96 2" fill="none" stroke="var(--swoosh-dark)" stroke-width="1"/>
    </svg>
  </div>
  <span class="label" style="left:12px; top:273px;">Business Card Front</span>

  <!-- Business card back -->
  <div class="piece card-back">
    <div class="brand"><span class="brand__dot"></span><span>Bluefern Trading<br>Partners, Ltd.</span></div>
  </div>
  <span class="label" style="left:12px; top:346px;">Business Card Back</span>

  <!-- Letterhead option 1 -->
  <div class="piece letterhead letterhead--one">
    <svg style="position:absolute;left:0;top:0;width:100%;height:14px" viewBox="0 0 285 14" preserveAspectRatio="none" aria-hidden="true">
      <path d="M0 0 L285 0 L285 2 C200 2 120 10 0 12Z" fill="var(--brand-blue)"/>
    </svg>
    <div class="brand"><span class="brand__dot"></span><span>Bluefern Trading<br>Partners, Ltd.</span></div>
    <div class="contact">
      742 Hollis St. - Suite 0830<br>
      New York, NY 10093<br>
      212-555-0147 Ext-305<br>
      sales@bluefernexample.com<br>
      bluefernexample.com
    </div>
    <svg class="wave" viewBox="0 0 285 60" preserveAspectRatio="none" aria-hidden="true">
      <path d="M0 22 C90 62 180 10 285 18 L285 60 L0 60Z" fill="var(--brand-blue)"/>
      <path d="M0 16 C90 56 180 4 285 12" fill="none" stroke="var(--swoosh-dark)" stroke-width="2.5"/>
    </svg>
  </div>
  <span class="label" style="left:262px; top:424px;">Letterhead Option 1</span>

  <!-- Letterhead option 2 -->
  <div class="piece letterhead letterhead--two">
    <div class="brand"><span class="brand__dot"></span><span>Bluefern Trading<br>Partners, Ltd.</span></div>
    <div class="faint-mark" aria-hidden="true"></div>
    <svg class="wave" viewBox="0 0 285 60" preserveAspectRatio="none" aria-hidden="true">
      <path d="M0 14 C80 4 190 58 285 24 L285 60 L0 60Z" fill="var(--brand-blue)"/>
      <path d="M0 8 C80 -2 190 52 285 18" fill="none" stroke="var(--swoosh-dark)" stroke-width="2.5"/>
    </svg>
  </div>
  <span class="label" style="left:590px; top:424px;">Letterhead Option 2</span>

  <!-- Envelope backs -->
  <div class="piece envelope-back envelope-back--white">
    <svg class="flap" viewBox="0 0 346 64" preserveAspectRatio="none" aria-hidden="true">
      <path d="M0 0 L346 0 L346 8 C260 8 220 30 173 30 C126 30 86 8 0 8Z" fill="var(--paper)" stroke="#d5d8de" stroke-width=".8"/>
    </svg>
  </div>
  <div class="piece envelope-back envelope-back--dark">
    <svg class="flap" viewBox="0 0 346 64" preserveAspectRatio="none" aria-hidden="true">
      <rect width="346" height="64" fill="var(--paper-shade)"/>
      <path d="M0 0 L346 0 L346 10 C260 10 220 36 173 36 C126 36 86 10 0 10Z" fill="var(--brand-navy)"/>
    </svg>
  </div>
  <div class="piece envelope-back envelope-back--blue">
    <svg class="flap" viewBox="0 0 346 64" preserveAspectRatio="none" aria-hidden="true">
      <path d="M0 0 L346 0 L346 10 C260 10 220 36 173 36 C126 36 86 10 0 10Z" fill="var(--brand-blue)"/>
    </svg>
    <div class="brand" style="top:42px;"><span class="brand__dot"></span><span>Bluefern Trading Partners, Ltd.</span></div>
  </div>
  <span class="label" style="left:1110px; top:158px;">Envelope Option 1</span>

  <!-- Envelope front -->
  <div class="piece envelope-front">
    <div class="brand"><span class="brand__dot"></span><span>Bluefern Trading<br>Partners, Ltd.</span></div>
    <div class="contact">
      742 Hollis St. - Suite 0830<br>
      New York, NY 10093
    </div>
    <svg class="wave" viewBox="0 0 356 40" preserveAspectRatio="none" aria-hidden="true">
      <path d="M0 18 C110 44 230 4 356 14 L356 40 L0 40Z" fill="var(--brand-blue)"/>
      <path d="M0 12 C110 38 230 -2 356 8" fill="none" stroke="var(--swoosh-dark)" stroke-width="2"/>
    </svg>
  </div>
  <span class="label" style="left:1090px; top:412px;">Envelope Option 3</span>

</body>
</html>
```